Termite Mailer September 2021

We need a clean modern looking flyer advertising termites via the mail.

Size should be 9"x6"

Our tagline is "The Smarter Approach to Pest Control"

Something along the stylistic design of these:

https://pics.hollowmarsh.example/Qa83LkTzWp

https://pics.hollowmarsh.example/Rn47VbXcMd

https://pics.hollowmarsh.example/Hj29PsYeUf

https://www.flintquillprint.example/wp-content/uploads/designs/img/Pest-Prevention-Postcard-PST-1003.jpg

Should include some of this verbiage:

HAVE YOU SCHEDULED YOUR ANNUAL TERMITE INSPECTION? - MAKE IT IN RED

DON'T WAIT. PROTECT YOUR HOME TODAY!

ABSOLUTELY FREE INSPECTION. NO OBLIGATION.

TERMITES CAN CAUSE SEVERE DAMAGE TO YOUR HOME.

BRINDLEVALE LOGO

THE SMARTER APPROACH TO PEST CONTROL.

PROTECT YOUR MOST VALUABLE ASSET.

10% DISCOUNT ON ANY SERVICE GUARANTEED IF YOU CALL TODAY.

INCLUDE A PICTURE OF A TERMITE AS WELL SOMEWHERE AND WOOD DAMAGE.

Target Market(s)

Homeowners in Southern California USA

Industry/Entity Type

Pest Control/Extermination

Font styles to use
Other font styles liked:
• Chaparral Pro Italic, Brava Slab

Requirements
Must have
• Clean design, picture of house, picture of Termite, 10% off coupon and call to action on the back
Should not have
• Bad looking houses, colors that don't match our logo

```html
<!DOCTYPE html>
<html lang="en">
<head>
<meta charset="utf-8">
<title>Brindlevale Termite Mailer</title>
<link rel="stylesheet" href="https://fonts.googleapis.com/css2?family=Bebas+Neue&family=Poppins:wght@400;500;700;800&display=swap">
<style>
  :root {
    --page-bg: #c6d5f2;
    --card-bg: #f0f1f5;
    --brand-red: #bd1622;
    --brand-blue: #204d9c;
    --logo-blue: #1f64ad;
    --brand-green: #7aba48;
    --white: #ffffff;
    --ink: #222222;
  }
  * { margin: 0; padding: 0; box-sizing: border-box; }
  html, body { width: 1200px; height: 1200px; overflow: hidden; background: var(--page-bg); }
  .mailer {
    position: absolute; left: 57px; top: 238px;
    width: 1086px; height: 724px;
    background: var(--card-bg);
    overflow: hidden;
    box-shadow: 0 6px 18px rgba(40, 60, 110, 0.18);
  }
  .hero-shapes { position: absolute; left: 0; top: 0; }
  .headline {
    position: absolute; left: 42px; top: 68px;
    font-family: "Bebas Neue", "Arial Narrow", sans-serif;
    font-size: 70px; line-height: 70px; color: var(--white);
    letter-spacing: 1px;
  }
  .benefits {
    position: absolute; left: 0; top: 315px; width: 618px; height: 170px;
    background: var(--brand-blue); padding: 24px 0 0 54px;
    font-family: "Bebas Neue", "Arial Narrow", sans-serif;
    font-size: 30px; line-height: 39px; color: var(--white); letter-spacing: 0.4px;
  }
  .photo { position: absolute; }
  .photo-damage { left: 653px; top: 355px; width: 209px; height: 130px;
    background: linear-gradient(160deg, #efe9e3 0%, #8a5a3a 45%, #4a3a36 100%); }
  .photo-termites { left: 881px; top: 355px; width: 205px; height: 130px;
    background: radial-gradient(circle at 60% 50%, #8a4a2a 0%, #4a2a1c 60%, #2e1c14 100%); }
  .brand-panel {
    position: absolute; left: 0; top: 501px; width: 410px; height: 223px;
    background: var(--white);
  }
  .brand-logo { position: absolute; left: 48px; top: 40px; display: flex; align-items: center; gap: 12px; }
  .brand-mark { width: 62px; height: 62px; border-radius: 50%; background: var(--brand-green); }
  .brand-name {
    font-family: "Poppins", sans-serif; font-weight: 700; color: var(--logo-blue);
    font-size: 27px; line-height: 30px;
  }
  .tagline {
    position: absolute; left: 48px; top: 126px;
    font-family: "Poppins", sans-serif; font-size: 15.5px; line-height: 23px; color: var(--ink);
  }
  .photo-technician { left: 410px; top: 501px; width: 208px; height: 223px;
    background: linear-gradient(90deg, #e9ebee 0%, #d7d9dd 55%, #6e4036 80%, #5a332c 100%); }
  .offer {
    position: absolute; left: 618px; top: 501px; width: 468px; height: 223px;
    background: var(--brand-green); padding: 14px 0 0 35px;
    font-family: "Poppins", sans-serif; color: var(--white);
  }
  .offer-rate { font-weight: 800; font-size: 70px; line-height: 64px; letter-spacing: -2px; }
  .offer-label { font-weight: 400; font-size: 20px; line-height: 24px; letter-spacing: 1px; margin-top: 4px; }
  .offer-terms { font-weight: 400; font-size: 24px; line-height: 32px; letter-spacing: 1.6px; }
  .offer-call { display: flex; align-items: baseline; gap: 4px; margin-top: 2px; }
  .offer-call-label { font-size: 18px; letter-spacing: 1px; }
  .offer-phone { font-weight: 700; font-size: 32px; letter-spacing: 2px; }
</style>
</head>
<body>
  <main class="mailer">
    <svg class="hero-shapes" width="1086" height="340" viewBox="0 0 1086 340">
      <polygon points="0,0 719,0 523,179 618,296 0,296" fill="var(--brand-red)"/>
      <polygon points="719,0 755,0 563,179 651,296 651,338 618,296 523,179" fill="var(--white)"/>
      <polygon points="755,0 1086,0 1086,338 651,338 651,296 563,179" fill="#6c7390" role="img" aria-label="Photo of a well-kept blue craftsman-style house with white trim and a wooden front door"/>
    </svg>
    <h1 class="headline">Have you scheduled<br>your annual<br>termite inspection?</h1>
    <section class="benefits">
      <p>Don't wait. Protect your home today!</p>
      <p>Absolutely free inspection. No obligation.</p>
      <p>Termites can cause severe damage to your home.</p>
    </section>
    <div class="photo photo-damage" role="img" aria-label="Close-up of termite-damaged wood"></div>
    <div class="photo photo-termites" role="img" aria-label="Close-up of termites on soil"></div>
    <section class="brand-panel">
      <div class="brand-logo">
        <span class="brand-mark"></span>
        <span class="brand-name">BRINDLEVALE<br>PEST CONTROL</span>
      </div>
      <p class="tagline">The Smarter Approach To Pest Control.<br>Protect Your Most Valuable Asset.</p>
    </section>
    <div class="photo photo-technician" role="img" aria-label="Pest control technician in protective suit spraying along a baseboard"></div>
    <section class="offer">
      <p class="offer-rate">10%</p>
      <p class="offer-label">DISCOUNT</p>
      <p class="offer-terms">ON ANY SERVICE<br>GUARANTEED IF YOU</p>
      <p class="offer-call"><span class="offer-call-label">CALL TODAY:</span><span class="offer-phone">714-555-0142</span></p>
    </section>
  </main>
</body>
</html>
```